website design for B&T Electric

A portfolio website for a high end commercial and residential electrical contracting company. The current site bandtelectric.example does not represent the current direction but the images in the gallery give you an idea of the work we do. Current logo will be uploaded shortly but is black text on white background.
Target Market(s)
General Contractors, Residential Home Owners, clients intersted in Quavis home automation.
Industry/Entity Type
Electrician
Coding
Coded - Design and coding required
Number of Pages Required
2 page
Font styles to use
Sans Serif
Colors
Designer to choose colors to be used in the design.
Requirements
Must have
- Portfolio section highlighting different service areas and products (Quavis Dwellsync, etc)

```html
<!DOCTYPE html>
<html lang="en">
<head>
<meta charset="utf-8">
<title>B&amp;T Electric</title>
<link href="https://fonts.googleapis.com/css2?family=Rufina:wght@400;700&family=Raleway:wght@400;500;700&display=swap" rel="stylesheet">
<style>
:root{
  --ink:#333333;
  --muted:#666666;
  --dark:#2e2e2e;
  --band:#f5f5f5;
  --white:#ffffff;
  --btn:#3a3a3a;
  --btn-alt:#777777;
  --footer-text:#cfcfcf;
}
*{margin:0;padding:0;box-sizing:border-box}
html,body{width:1200px;height:2812px;overflow:hidden;background:var(--white)}
body{font-family:"Raleway",sans-serif;color:var(--ink);position:relative}
section,header,footer{position:absolute;left:0;width:1200px}

/* header */
.site-header{top:0;height:72px;background:var(--white);border-bottom:1px solid #e6e6e6}
.brand{position:absolute;left:75px;top:0;height:72px;display:flex;align-items:center;gap:12px}
.brand-mark{width:18px;height:18px;background:var(--dark)}
.brand-name{font-family:"Raleway",sans-serif;font-weight:700;font-size:28px;color:var(--dark)}
.main-nav{position:absolute;right:50px;top:26px;display:flex;gap:62px}
.main-nav a{font-family:"Rufina",serif;font-size:16px;color:var(--ink);text-decoration:none;letter-spacing:.5px}

/* hero */
.hero{top:72px;height:504px;background:linear-gradient(180deg,#2c4a7c 0%,#3d5a86 35%,#5a4a3c 65%,#2c2b22 100%)}
.hero h1{position:absolute;top:160px;width:100%;text-align:center;font-family:"Rufina",serif;font-weight:400;font-size:72px;color:var(--white)}
.hero p{position:absolute;top:246px;left:270px;width:660px;text-align:center;font-size:27px;line-height:34px;color:var(--white);font-weight:500}
.hero-dots{position:absolute;top:444px;left:563px;display:flex;gap:8px}
.hero-dots i{width:10px;height:10px;border-radius:50%;background:#222}
.hero-dots i:first-child{background:var(--white)}

.section-title{position:absolute;width:100%;text-align:center;font-family:"Rufina",serif;font-weight:400;font-size:32px;color:var(--ink)}
.btn{position:absolute;background:var(--btn);color:var(--white);font-family:"Rufina",serif;font-size:16px;text-align:center;line-height:42px;height:42px}

/* welcome */
.welcome{top:576px;height:309px}
.welcome .section-title{top:46px}
.welcome p{position:absolute;top:102px;left:165px;width:870px;text-align:center;font-size:14px;line-height:25px;color:var(--muted)}
.welcome .btn{left:530px;top:209px;width:140px}

/* services */
.services{top:885px;height:410px;background:var(--band)}
.services .section-title{top:36px}
.service{position:absolute;width:300px}
.service svg{position:absolute;left:0;top:4px;width:44px;height:44px;fill:#3a3a3a}
.service h3{position:absolute;left:86px;top:0;font-family:"Rufina",serif;font-weight:400;font-size:23px;color:var(--ink)}
.service p{position:absolute;left:86px;top:34px;width:200px;font-size:13px;line-height:21px;color:var(--muted)}

/* gallery */
.gallery{top:1295px;height:663px}
.gallery .section-title{top:34px}
.filters{position:absolute;top:104px;left:427px;display:flex}
.filters span{font-size:14px;color:var(--muted);padding:0 12px;line-height:32px}
.filters .active{background:var(--btn);color:var(--white);padding:0 18px}
.photo{position:absolute;width:341px;height:214px}

/* certified */
.certified{top:1958px;height:632px;background:var(--band)}
.panel-photo{position:absolute;left:75px;width:392px;height:235px}
.certified h2{position:absolute;left:510px;top:52px;font-family:"Rufina",serif;font-weight:400;font-size:33px;color:var(--ink)}
.tabs{position:absolute;left:510px;top:125px;display:flex;gap:4px}
.tabs span{font-family:"Rufina",serif;font-size:16px;color:var(--white);height:43px;line-height:43px;padding:0 18px;background:var(--btn-alt)}
.tabs .active{background:var(--btn)}
.certified .intro{position:absolute;left:510px;top:192px;width:610px;font-size:15px;line-height:27px;color:var(--ink)}
.feature-list{position:absolute;left:510px;top:258px;width:615px;list-style:none}
.feature-list li{position:relative;padding-left:22px;font-size:13px;line-height:26px;color:var(--muted);margin-bottom:24px}
.feature-list li::before{content:"";position:absolute;left:0;top:9px;width:8px;height:8px;border:2px solid #555;border-radius:50%}
.certified .btn{left:510px;top:523px;width:140px;height:43px;line-height:43px}

/* footer */
.site-footer{top:2590px;height:222px;background:var(--dark);color:var(--footer-text)}
.foot-col{position:absolute;top:40px}
.foot-col h4{font-size:13px;font-weight:700;color:var(--white);letter-spacing:.5px;margin-bottom:12px}
.foot-col p{font-size:12px;line-height:28px}
.contact-line{display:flex;gap:14px;align-items:center}
.contact-line svg{width:12px;height:12px;fill:var(--footer-text)}
.social{display:flex;gap:14px;margin:4px 0 22px}
.social i{width:16px;height:16px;border-radius:50%;background:var(--footer-text)}
.foot-col .copy{line-height:20px}
.page-tag{position:absolute;right:16px;bottom:16px;font-size:13px;color:var(--footer-text)}
</style>
</head>
<body>

<header class="site-header">
  <div class="brand"><i class="brand-mark"></i><span class="brand-name">B&amp;T Electric</span></div>
  <nav class="main-nav">
    <a href="#">HOME</a><a href="#">GALLERY</a><a href="#">SPECIALTY SERVICES</a><a href="#">ABOUT</a><a href="#">CONTACT</a>
  </nav>
</header>

<section class="hero" role="img" aria-label="Modern hillside home at dusk with warm exterior lighting">
  <h1>B&amp;T Electric</h1>
  <p>We are a high end commercial and residential electrical contracting company.</p>
  <div class="hero-dots"><i></i><i></i><i></i><i></i></div>
</section>

<section class="welcome">
  <h2 class="section-title">Welcome to Our Website</h2>
  <p>B &amp; T Electric is a full service electrical contracting shop. We offer commercial, residential, light industrial, and agricultural services. We're Quavis Dwellsync and Quavis Motorized Shades certified, as well as an authorized Powerhaven generator dealer. We've served the Marlow Valley and the Central Basin for over a decade.</p>
  <div class="btn">Read More</div>
</section>

<section class="services">
  <h2 class="section-title">Our Services</h2>
  <div class="service" style="left:94px;top:120px">
    <svg viewBox="0 0 44 44"><path d="M8 4h28v38H8z M13 9v4h4V9z M20 9v4h4V9z M27 9v4h4V9z M13 16v4h4v-4z M20 16v4h4v-4z M27 16v4h4v-4z M13 23v4h4v-4z M20 23v4h4v-4z M27 23v4h4v-4z M19 33v9h6v-9z" fill-rule="evenodd"/></svg>
    <h3>Commercial</h3><p>Lorem ipsum dolor sit amet, consect- etuer adipiscing elit, sed diam nonummy..</p>
  </div>
  <div class="service" style="left:456px;top:120px">
    <svg viewBox="0 0 44 44"><path d="M22 6 2 24h6v16h11V30h6v10h11V24h6L34 14V7h-5v3z"/></svg>
    <h3>Residential</h3><p>Lorem ipsum dolor sit amet, consect- etuer adipiscing elit, sed diam nonummy..</p>
  </div>
  <div class="service" style="left:818px;top:120px">
    <svg viewBox="0 0 44 44"><path d="M22 4c-9 8-13 15-13 22a13 13 0 0 0 11 12v4h4v-4a13 13 0 0 0 11-12c0-7-4-14-13-22z"/><path d="M22 14v22M22 24l6-5M22 30l-6-5" stroke="#f5f5f5" stroke-width="2" fill="none"/></svg>
    <h3>Landscape</h3><p>Lorem ipsum dolor sit amet, consect- etuer adipiscing elit, sed diam nonummy..</p>
  </div>
  <div class="service" style="left:94px;top:253px">
    <svg viewBox="0 0 44 44"><path d="M2 6h32v4H2z M4 10h28v14H4z M31 20h8l3 8H28z M34 28h2v12h-2z M30 40h10v2H30z M6 24h2v16H6z"/></svg>
    <h3>Quavis Shades</h3><p>Lorem ipsum dolor sit amet, consect- etuer adipiscing elit, sed diam nonummy..</p>
  </div>
  <div class="service" style="left:456px;top:253px">
    <svg viewBox="0 0 44 44"><rect x="4" y="10" width="28" height="24" rx="4"/><circle cx="18" cy="22" r="7" fill="#f5f5f5"/><circle cx="18" cy="22" r="3"/><path d="M38 12l-4 10h4l-3 10 7-13h-4l3-7z"/></svg>
    <h3>Generators</h3><p>Lorem ipsum dolor sit amet, consect- etuer adipiscing elit, sed diam nonummy..</p>
  </div>
  <div class="service" style="left:818px;top:253px">
    <svg viewBox="0 0 44 44"><path d="M22 4a13 13 0 0 0-8 23c2 2 3 4 3 6h10c0-2 1-4 3-6a13 13 0 0 0-8-23zm-5 31h10v3H17zm2 4h6v3h-6z"/></svg>
    <h3>LED Lighting</h3><p>Lorem ipsum dolor sit amet, consect- etuer adipiscing elit, sed diam nonummy..</p>
  </div>
</section>

<section class="gallery">
  <h2 class="section-title">Photo Gallery</h2>
  <div class="filters"><span class="active">All</span><span>Commercial</span><span>Residential</span><span>Landscape</span></div>
  <div class="photo" style="left:75px;top:169px;background:linear-gradient(180deg,#1f2a44,#4a3a2a 60%,#2a2420)" role="img" aria-label="Stone home lit at night"></div>
  <div class="photo" style="left:431px;top:169px;background:linear-gradient(180deg,#5d8fd0,#9a7e66 55%,#5e5e55)" role="img" aria-label="Stone commercial building with arched windows"></div>
  <div class="photo" style="left:786px;top:169px;background:linear-gradient(180deg,#9fb8d8,#8a6c58 50%,#6b5a4c)" role="img" aria-label="Stone building with arched roofline"></div>
  <div class="photo" style="left:75px;top:394px;background:linear-gradient(180deg,#4f7fc4,#9cb6d8 45%,#c9c4ba 70%,#6f6a5e)" role="img" aria-label="Modern office building under blue sky"></div>
  <div class="photo" style="left:431px;top:394px;background:linear-gradient(180deg,#6a6a6a,#b8b4ae 55%,#e8e6e2)" role="img" aria-label="Modern lobby with lit reception desk"></div>
  <div class="photo" style="left:786px;top:394px;background:linear-gradient(180deg,#2d5aa8,#324060 50%,#3a3226)" role="img" aria-label="Modern home with landscape lighting at dusk"></div>
</section>

<section class="certified">
  <div class="panel-photo" style="top:61px;background:linear-gradient(135deg,#c9a66b,#b38a4e 60%,#8e6a38)" role="img" aria-label="Lighting keypad control panel on a wall"></div>
  <div class="panel-photo" style="top:331px;background:linear-gradient(135deg,#e6ddd0,#cbbca6 60%,#8a7058)" role="img" aria-label="Wall mounted lighting keypad"></div>
  <h2>Quavis Dwellsync Certified</h2>
  <div class="tabs"><span class="active">Features</span><span>More Information</span></div>
  <p class="intro">We're proudly certified to install Quavis Dwellsync systems. Dwellsync gives you complete control over your home lighting with just a few simple buttons.</p>
  <ul class="feature-list">
    <li>Manage the shades, lighting, and temperature in your house remotely using your tablet or phone.</li>
    <li>Set your lights and shades to work exactly how you want, at the times you want. For example, a single button that lowers all of the lights in your entertainment room, lowers the shades, and turns the kitchen lights to low for when you want to watch a movie.</li>
    <li>Control your lights based on time or day of the week.</li>
    <li>Raise and lower your shades based on the time of day.</li>
  </ul>
  <div class="btn">Read More</div>
</section>

<footer class="site-footer">
  <div class="foot-col" style="left:75px"><h4>SITE MAP</h4><p>Home<br>Gallery<br>Specialty Services<br>About<br>Contact</p></div>
  <div class="foot-col" style="left:255px"><h4>SPECIALTY SERVICES</h4><p>Quavis Dwellsync<br>Quavis Veilmotion Motorized Shades<br>LED Lighting<br>Emergency Generators</p></div>
  <div class="foot-col" style="left:531px"><h4>GALLERY</h4><p>Commercial<br>Residential<br>Landscape</p></div>
  <div class="foot-col" style="left:684px"><h4>CONTACT INFO</h4>
    <p style="line-height:19px;margin-bottom:10px">2215 Hangar Road<br>PO Box 4410 Marlow, ID 83999</p>
    <p class="contact-line"><svg viewBox="0 0 12 12"><path d="M2 1h3l1 3-2 1a7 7 0 0 0 3 3l1-2 3 1v3a1 1 0 0 1-1 1A10 10 0 0 1 1 2a1 1 0 0 1 1-1z"/></svg>(555) 014-2290</p>
    <p class="contact-line"><svg viewBox="0 0 12 12"><path d="M0 2h12v8H0z"/></svg>info@bandtelectric.example</p>
  </div>
  <div class="foot-col" style="left:924px"><h4>FOLLOW US</h4>
    <div class="social"><i></i><i></i><i></i><i></i><i></i><i></i></div>
    <p class="copy">Copyright © 2017, Company Name.<br>All Right Reserved</p>
  </div>
  <div class="page-tag">X10</div>
</footer>

</body>
</html>
```